I want to revise my business card design and get a more modern and up to date design.

Brolvane Handyman Sevices originated from a family-owned and operated contractor business, performing home renovation, addition, and construction work in the NYC area since 2004. Today, we specialize in reliable and affordable handyman services for residential and commercial clients In 2014, we expanded to northern New Jersey. In 2016, we brought quality home improvement and repair services to new Bucks County, PA, and nearby New Jersey areas.
Target Market(s)
Home owners and business that might be looking for a General contractor, handyman, cleaning services and Home maintenance and property.
Industry/Entity Type
Construction Company
Contact Information for Business Card
I am open to new ideas
Colors
Designer to choose colors to be used in the design.
Look and feel
Each slider illustrates characteristics of the customer's brand and the style your logo design should communicate.

```html
<!DOCTYPE html>
<html lang="en">
<head>
<meta charset="utf-8">
<title>Brolvane Handyman Sevices – Business Card</title>
<link href="https://fonts.googleapis.com/css2?family=Lato:wght@400;700;900&display=swap" rel="stylesheet">
<style>
  :root {
    --backdrop: #7a7a7a;
    --card-white: #ffffff;
    --card-black: #000000;
    --brand-red: #e3232b;
    --ink: #111111;
    --ink-soft: #4a4a4a;
    --rule: #b5a79a;
    --badge-grey: #d9d9d9;
    --faint: #1b1b1b;
  }
  html, body {
    margin: 0;
    padding: 0;
    width: 1200px;
    height: 1200px;
    overflow: hidden;
    background: var(--backdrop);
    font-family: "Lato", sans-serif;
  }
  .canvas { position: relative; width: 1200px; height: 1200px; }
  .card {
    position: absolute;
    top: 310px;
    width: 364px;
    height: 594px;
    box-shadow: 2px 3px 6px rgba(0,0,0,0.45);
    overflow: hidden;
  }
  .card--front { left: 234px; background: var(--card-white); }
  .card--back { left: 627px; width: 369px; height: 596px; background: var(--card-black); }

  .brand {
    position: absolute;
    top: 120px;
    left: 0;
    width: 100%;
    text-align: center;
  }
  .brand__row { display: inline-flex; align-items: center; gap: 14px; }
  .brand__dot {
    width: 46px; height: 46px; border-radius: 50%;
    background: var(--brand-red);
  }
  .brand__name {
    font-weight: 900;
    font-size: 50px;
    color: var(--ink);
    letter-spacing: -0.5px;
    line-height: 1;
  }
  .brand__tagline {
    margin-top: 10px;
    font-size: 11px;
    letter-spacing: 3.2px;
    color: var(--ink-soft);
  }

  .contact {
    position: absolute;
    top: 352px;
    left: 0;
    width: 100%;
    text-align: center;
  }
  .contact__name {
    font-size: 25px;
    color: var(--brand-red);
    margin: 0;
    font-weight: 400;
  }
  .contact__rule {
    width: 152px; height: 1px;
    background: var(--rule);
    margin: 11px auto 8px;
  }
  .contact__line { font-size: 17px; color: var(--ink); line-height: 22px; margin: 0; }
  .contact__rule--bottom { margin-top: 10px; }

  .badges {
    position: absolute;
    top: 472px;
    left: 0;
    width: 100%;
  }
  .badge { position: absolute; background: var(--badge-grey); border-radius: 3px; }
  .badge--listing { left: 76px; top: 14px; width: 102px; height: 26px; }
  .badge--rating { left: 195px; top: 0; width: 92px; height: 40px; background: var(--brand-red); }
  .badge--services { left: 88px; top: 48px; width: 188px; height: 26px; }

  .back__mark {
    position: absolute;
    left: 50%;
    top: 170px;
    transform: translateX(-50%);
    width: 150px; height: 150px;
    border-radius: 50%;
    background: var(--brand-red);
  }
  .back__name {
    position: absolute;
    top: 345px; left: 0; width: 100%;
    text-align: center;
    font-weight: 900;
    font-size: 34px;
    color: #ffffff;
  }
  .back__services {
    position: absolute;
    top: 473px; left: 0; width: 100%;
    text-align: center;
    color: #ffffff;
    font-size: 17px;
    line-height: 21.5px;
  }
  .back__services p { margin: 0; }
  .sep { color: var(--brand-red); font-size: 14px; padding: 0 3px; }
</style>
</head>
<body>
<main class="canvas">
  <section class="card card--front">
    <div class="brand">
      <div class="brand__row">
        <span class="brand__dot"></span>
        <span class="brand__name">Brolvane</span>
      </div>
      <div class="brand__tagline">HANDYMAN SERVICES</div>
    </div>
    <div class="contact">
      <h1 class="contact__name">Marco Delgado</h1>
      <div class="contact__rule"></div>
      <p class="contact__line">(215) 555- 0148</p>
      <p class="contact__line">brolvanehandymannyc@mail.com</p>
      <div class="contact__rule contact__rule--bottom"></div>
    </div>
    <div class="badges">
      <span class="badge badge--listing"></span>
      <span class="badge badge--rating"></span>
      <span class="badge badge--services"></span>
    </div>
  </section>

  <section class="card card--back">
    <div class="back__mark"></div>
    <div class="back__name">Brolvane</div>
    <div class="back__services">
      <p>Commercial and Residential Contractor,</p>
      <p>Handyman, Technician</p>
      <p>Repair <span class="sep">●</span> Improve <span class="sep">●</span> Maintain <span class="sep">●</span> Remodel</p>
    </div>
  </section>
</main>
</body>
</html>
```